GPS business card

Brantor Works is the name of my company
Navs that slot right in!

My Business is supply and install of IN DASH GPS SYSTEMS.
Small family based business that is mobile.

GPS touch screens that are built into the dash.
I have a logo I want Utilized
Wanting colours too

I have screens for all makes and models of vehicles.

I have attached a current business card and some photo's of the work I do.

Target Market(s)

new and used car buyers

Industry/Entity Type

Business

Requirements
Must have
• Name: Ross Brantor

Mob: 0438 512 604
email: rossbrantor@mailvale.net

Must use logo

```html
<!DOCTYPE html>
<html lang="en">
<head>
<meta charset="utf-8">
<title>Brantor Works – Business Card</title>
<link href="https://fonts.googleapis.com/css2?family=Open+Sans:wght@400;600;700&family=Michroma&display=swap" rel="stylesheet">
<style>
  :root {
    --page-bg: #ececec;
    --card-bg: #050505;
    --dash-dark: #111214;
    --dash-mid: #26282b;
    --brand-blue: #2a8fd8;
    --tag-blue: #6cc3f0;
    --accent-orange: #f08a2c;
    --text-white: #f2f2f2;
    --text-grey: #c9c9c9;
  }
  * { margin: 0; padding: 0; box-sizing: border-box; }
  html, body {
    width: 1200px;
    height: 1000px;
    overflow: hidden;
    background: var(--page-bg);
  }
  .canvas {
    position: relative;
    width: 1200px;
    height: 1000px;
  }
  .business-card {
    position: absolute;
    left: 50px;
    top: 162px;
    width: 1100px;
    height: 676px;
    background: var(--card-bg);
    overflow: hidden;
    box-shadow: 0 10px 30px rgba(0,0,0,0.25);
  }
  .dashboard-photo {
    position: absolute;
    left: 0;
    top: 200px;
    width: 1100px;
    height: 476px;
    background:
      radial-gradient(ellipse 38% 60% at 55% 55%, var(--dash-mid) 0%, rgba(38,40,43,0.4) 55%, transparent 80%),
      linear-gradient(180deg, var(--card-bg) 0%, var(--dash-dark) 30%, var(--dash-dark) 85%, var(--card-bg) 100%);
    opacity: 0.9;
  }
  .brand {
    position: absolute;
    right: 26px;
    top: 52px;
    display: flex;
    align-items: center;
    gap: 22px;
  }
  .brand-dot {
    width: 70px;
    height: 70px;
    border-radius: 50%;
    background: var(--accent-orange);
  }
  .brand-name {
    font-family: "Open Sans", sans-serif;
    font-weight: 700;
    font-size: 68px;
    line-height: 1;
    color: var(--brand-blue);
    letter-spacing: 0.5px;
  }
  .brand-tagline {
    position: absolute;
    right: 22px;
    top: 208px;
    font-family: "Michroma", sans-serif;
    font-size: 22px;
    letter-spacing: 2px;
    color: var(--tag-blue);
  }
  .contact {
    position: absolute;
    left: 42px;
    top: 440px;
    font-family: "Open Sans", sans-serif;
  }
  .person-name {
    font-size: 50px;
    font-weight: 400;
    font-variant: small-caps;
    line-height: 1;
    letter-spacing: 1px;
  }
  .person-first { color: var(--text-white); }
  .person-last { color: var(--accent-orange); }
  .person-role {
    margin-top: 10px;
    font-size: 16px;
    letter-spacing: 3px;
    color: var(--text-grey);
    text-transform: uppercase;
  }
  .contact-lines {
    margin-top: 48px;
    font-size: 22px;
    letter-spacing: 2px;
    line-height: 1.4;
    color: var(--text-white);
    list-style: none;
  }
</style>
</head>
<body>
  <main class="canvas">
    <section class="business-card">
      <div class="dashboard-photo" role="img" aria-label="Dim photo of a car dashboard with a built-in GPS touch screen, air vents and steering wheel"></div>

      <div class="brand">
        <span class="brand-dot"></span>
        <span class="brand-name">Brantor Works</span>
      </div>
      <p class="brand-tagline">IN DASH GPS SYSTEMS</p>

      <div class="contact">
        <h1 class="person-name"><span class="person-first">Ross</span> <span class="person-last">Brantor</span></h1>
        <p class="person-role">Installation Technician</p>
        <ul class="contact-lines">
          <li>0438 512 604</li>
          <li>rossbrantor@mailvale.net</li>
        </ul>
      </div>
    </section>
  </main>
</body>
</html>
```